Landing page redesign

Hello, we would like a landing page redesigned. We already have one, but want to get some new design layouts and ideas as this one is outdated. You have full creative flexibility, do not feel the need to copy this one at all, we want to see new ideas and make this landing page look great!

Here is the link to the current one: https://go.brightfieldlead.com/criminal-orlando

```html
<!DOCTYPE html>
<html lang="en">
<head>
<meta charset="utf-8">
<title>Harlow Bennett — Dedicated Lawyers in Orlando</title>
<link href="https://fonts.googleapis.com/css2?family=Cinzel:wght@400;500&family=Montserrat:ital,wght@0,400;0,500;0,600;0,700;1,400&display=swap" rel="stylesheet">
<style>
:root{
  --navy:#0b1a3a;
  --navy-deep:#081530;
  --blue:#0b3a8a;
  --blue-line:#5f82c4;
  --red:#a1050f;
  --ink:#1a1f2e;
  --muted:#4a5060;
  --grey-bg:#e4e5e8;
  --white:#ffffff;
  --star:#e8641b;
}
*{box-sizing:border-box;margin:0;padding:0}
html,body{width:1200px;height:4511px;overflow:hidden}
body{position:relative;font-family:"Montserrat",sans-serif;color:var(--ink);background:var(--white)}
.abs{position:absolute}
.serif{font-family:"Cinzel",serif;font-weight:400}
.eyebrow{font-size:15px;letter-spacing:3px;color:var(--blue);text-transform:uppercase}
.section-title{font-family:"Cinzel",serif;font-size:40px;letter-spacing:1px;color:var(--ink);line-height:1}
.rule{height:2px;background:linear-gradient(90deg,transparent,#8c93a3 20%,#8c93a3 80%,transparent)}
.btn{display:flex;align-items:center;justify-content:center;font-weight:700;font-size:13px;letter-spacing:.5px;color:var(--white);text-transform:uppercase;border-radius:4px}
.btn-navy{background:var(--navy)}
.btn-red{background:var(--red)}

/* header / hero */
.hero{left:0;top:0;width:1200px;height:720px;background:
 radial-gradient(ellipse 300px 260px at 880px 260px,rgba(255,190,80,.35),transparent 70%),
 radial-gradient(ellipse 700px 220px at 600px 600px,rgba(220,60,90,.35),transparent 70%),
 linear-gradient(180deg,#0c1c4e 0%,#142a6a 45%,#2b1c58 70%,#0d1a45 100%)}
.hero-shade{left:0;top:0;width:760px;height:720px;background:linear-gradient(90deg,rgba(8,20,60,.75),rgba(8,20,60,0))}
.brand{display:flex;align-items:center;gap:14px}
.brand-mark{width:28px;height:28px;border:2px solid currentColor}
.brand-name{font-family:"Cinzel",serif;font-size:20px;letter-spacing:2px}
.nav{top:36px;display:flex;font-size:14px;font-weight:500;color:var(--white)}
.nav a{position:absolute;color:inherit;text-decoration:none;white-space:nowrap}
.nav .active{font-weight:700}
.nav .active::after{content:"";position:absolute;left:12px;right:12px;bottom:-7px;height:2px;background:var(--white)}
.phone{left:968px;top:28px;display:flex;align-items:center;gap:12px;color:var(--white);font-weight:600;font-size:19px}
.phone-icon{width:32px;height:32px;border-radius:50%;background:#1d4aa8;display:flex;align-items:center;justify-content:center}
.hero-copy{left:70px;top:196px;width:600px;text-align:center;color:var(--white)}
.hero-kicker{font-size:22px;letter-spacing:3px}
.hero-title{font-family:"Cinzel",serif;font-size:50px;line-height:54px;margin-top:18px;letter-spacing:1px}
.hero-text{font-size:18px;line-height:29px;margin-top:24px;opacity:.95}

/* about */
.about-text{left:625px;top:806px;width:480px}
.about-text p{font-size:14.5px;line-height:23.5px;color:var(--muted);margin-top:12px}

/* practice */
.practice{left:0;top:1267px;width:1200px;height:576px;background:var(--blue);color:var(--white)}
.center{text-align:center;width:1200px;left:0}
.card{border:1px solid var(--blue-line);text-align:center;color:var(--white)}
.card-red{background:var(--red);border:none}
.card-icon{margin:0 auto;width:52px;height:52px;border:2px solid var(--white);border-radius:50%}
.card h3{font-size:18px;font-weight:700;line-height:23px;margin-top:20px}
.card .bar{width:20px;height:2px;background:var(--white);margin:10px auto}
.card p{font-size:11px;line-height:15px;padding:0 50px;opacity:.9}
.card .card-btn{margin:16px auto 0;width:120px;height:32px;border:1.5px solid var(--white);border-radius:3px;font-size:10px;font-weight:700;display:flex;align-items:center;justify-content:center}
.chev{width:20px;height:28px}

/* why */
.why-list{list-style:none;width:316px}
.why-list li{height:35px;border-bottom:1px solid #c4c8d2;display:flex;align-items:center;font-size:15px;font-weight:600;gap:20px;padding-left:8px}
.why-list li:last-child{border-bottom:none}
.why-list li::before{content:"";width:6px;height:6px;background:var(--red)}

/* testimonials */
.testi{left:0;top:2469px;width:1200px;height:644px;background:
 linear-gradient(180deg,var(--grey-bg) 0%,rgba(228,229,232,.7) 40%,rgba(190,194,202,.9) 100%)}
.quote-card{left:266px;top:2721px;width:652px;height:261px;background:var(--white);text-align:center;box-shadow:0 4px 14px rgba(0,0,0,.12)}
.round-arrow{width:56px;height:56px;border-radius:50%;background:rgba(255,255,255,.75);display:flex;align-items:center;justify-content:center}

/* blogs */
.blog{border:1px solid #c9ccd4;background:var(--white)}
.blog-img{height:196px}
.blog-date{position:absolute;left:50px;top:190px;width:82px;height:18px;background:var(--navy);color:var(--white);font-size:9px;font-weight:700;display:flex;align-items:center;justify-content:center}
.blog h4{font-size:14.5px;font-weight:700;line-height:20px;padding:22px 38px 0}
.blog p{font-size:10.5px;line-height:17px;color:var(--muted);padding:10px 38px 0}
.blog .btn{position:absolute;left:38px;bottom:24px;width:128px;height:34px;font-size:11px;background:var(--blue)}

/* consult */
.consult{left:109px;top:3767px;width:972px;height:534px;background:var(--blue);color:var(--white);border-bottom:5px solid var(--red)}
.field{font-size:14px;color:var(--white);border-bottom:1.5px solid #c9d3ea;padding-bottom:10px}

/* footer */
.footer{left:0;top:4205px;width:1200px;height:306px;background:var(--navy)}
.foot-nav{font-size:14px;font-weight:500;color:var(--white)}
.foot-nav a{position:absolute;color:inherit;text-decoration:none;white-space:nowrap}
.legal{font-size:11px;color:#c7cdda}
</style>
</head>
<body>

<!-- HEADER + HERO -->
<section class="abs hero" role="img" aria-label="Night view of the Orlando skyline reflected in a lake"></section>
<div class="abs hero-shade"></div>

<div class="abs brand" style="left:100px;top:30px;color:var(--white)">
  <span class="brand-mark"></span><span class="brand-name">Harlow Bennett</span>
</div>
<nav class="abs nav" style="left:0;width:1200px">
  <a class="active" style="left:382px">HOME</a>
  <a style="left:466px">ABOUT US</a>
  <a style="left:580px">PRACTICE AREAS</a>
  <a style="left:739px">BLOGS</a>
  <a style="left:829px">CONTACT US</a>
</nav>
<div class="abs phone">
  <span class="phone-icon"><svg width="16" height="16" viewBox="0 0 24 24"><path fill="#fff" d="M6.6 10.8a15 15 0 0 0 6.6 6.6l2.2-2.2c.3-.3.7-.4 1-.2 1.1.4 2.3.6 3.6.6.6 0 1 .4 1 1V20c0 .6-.4 1-1 1A17 17 0 0 1 3 4c0-.6.4-1 1-1h3.5c.6 0 1 .4 1 1 0 1.3.2 2.5.6 3.6.1.3 0 .7-.2 1z"/></svg></span>
  (555) 014-2277
</div>

<div class="abs hero-copy">
  <div class="hero-kicker serif">HARLOW BENNETT</div>
  <h1 class="hero-title">DEDICATED LAWYERS<br>IN ORLANDO</h1>
  <p class="hero-text">Lorem ipsum dolor sit amet, consectetur adipiscing<br>elit, sed do eiusmod tempor incididunt</p>
</div>
<a class="abs btn btn-red" style="left:238px;top:455px;width:258px;height:62px;font-size:16px;gap:8px">BOOK APPOINTMENT <svg width="16" height="14" viewBox="0 0 16 14"><path d="M1 7h13M9 2l5 5-5 5" stroke="#fff" stroke-width="2" fill="none"/></svg></a>

<!-- ABOUT -->
<svg class="abs" style="left:0;top:720px" width="600" height="547" viewBox="0 0 600 547">
  <polygon points="420,0 445,0 590,261 365,547 340,547 565,261" fill="#b3b8c3"/>
  <polygon points="0,0 420,0 565,261 340,547 0,547" fill="#b89a82" role="img" aria-label="Attorney reviewing documents with a client at a desk"/>
  <polygon points="0,0 420,0 565,261 340,547 0,547" fill="url(#aboutShade)"/>
  <defs><linearGradient id="aboutShade" x1="0" y1="0" x2="1" y2="1"><stop offset="0" stop-color="#d9c7b2" stop-opacity=".6"/><stop offset="1" stop-color="#3a4258" stop-opacity=".6"/></linearGradient></defs>
</svg>
<div class="abs about-text">
  <div class="eyebrow">Who we are</div>
  <h2 class="section-title" style="margin-top:6px">ABOUT BENNETT LAW</h2>
  <div class="rule" style="width:460px;margin-top:8px"></div>
  <p style="margin-top:22px">Lorem ipsum dolor sit amet, consectetur adipiscing elit, sed do eiusmod tempor incididunt ut labore et dolore magna aliqua. Ut enim ad minim veniam, quis nostrud exercitation ullamco laboris nisi ut aliquip ex ea commodo consequat.</p>
  <p>Duis aute irure dolor in reprehenderit in voluptate velit esse cillum dolore eu fugiat nulla pariatur. Excepteur sint occaecat cupidatat non proident, sunt in culpa qui officia deseruntdicta sunt exp</p>
</div>
<a class="abs btn btn-navy" style="left:632px;top:1105px;width:167px;height:44px">LEARN MORE</a>

<!-- PRACTICE AREAS -->
<section class="abs practice">
  <div class="abs center eyebrow" style="top:50px;color:#c9d5ef;font-size:14px">What we do</div>
  <h2 class="abs center section-title" style="top:80px;color:var(--white)">PRACTICE AREAS</h2>
  <div class="abs rule" style="left:470px;top:124px;width:260px;background:linear-gradient(90deg,transparent,#fff 20%,#fff 80%,transparent)"></div>

  <svg class="abs chev" style="left:46px;top:313px" viewBox="0 0 20 28"><path d="M16 2 4 14l12 12" stroke="#fff" stroke-width="3.5" fill="none"/></svg>
  <svg class="abs chev" style="left:1122px;top:313px" viewBox="0 0 20 28"><path d="M4 2l12 12L4 26" stroke="#fff" stroke-width="3.5" fill="none"/></svg>

  <div class="abs card" style="left:100px;top:171px;width:324px;height:302px;padding-top:28px">
    <div class="card-icon"></div>
    <h3>CRIMINAL DEFENSE<br>AND ASSAULT</h3><div class="bar"></div>
    <p>Lorem ipsum dolor sit amet, consectetur adipiscing elit, sed do eiusmod tempor incididunt ut labore et dolore magna aliqua. Ut enim ad minim veniam.</p>
    <div class="card-btn">LEARN MORE</div>
  </div>
  <div class="abs card card-red" style="left:438px;top:154px;width:324px;height:342px;padding-top:45px">
    <div class="card-icon"></div>
    <h3>PERSONAL<br>INJURY</h3><div class="bar"></div>
    <p>Lorem ipsum dolor sit amet, consectetur adipiscing elit, sed do eiusmod tempor incididunt ut labore et dolore magna aliqua. Ut enim ad minim veniam.</p>
    <div class="card-btn">LEARN MORE</div>
  </div>
  <div class="abs card" style="left:781px;top:171px;width:324px;height:302px;padding-top:25px">
    <div class="card-icon"></div>
    <h3>DIVORCE AND<br>FAMILY LAW</h3><div class="bar"></div>
    <p>Lorem ipsum dolor sit amet, consectetur adipiscing elit, sed do eiusmod tempor incididunt ut labore et dolore magna aliqua. Ut enim ad minim veniam.</p>
    <div class="card-btn">LEARN MORE</div>
  </div>
</section>

<!-- WHY CHOOSE US -->
<div class="abs" style="left:112px;top:1966px;width:480px">
  <div class="eyebrow">Why we are</div>
  <h2 class="section-title" style="margin-top:4px">WHY CHOOSE US</h2>
  <div class="rule" style="width:330px;margin-top:6px"></div>
  <p style="font-size:14.5px;line-height:24px;color:var(--muted);margin-top:22px;padding-left:8px">Lorem ipsum dolor sit amet, consectetur adipiscing elit, sed do eiusmod tempor incididunt ut labore et dolore magna</p>
  <ul class="why-list" style="margin-top:16px">
    <li>15+ Years Experience</li>
    <li>Flexible Payment Plans</li>
    <li>Flat Rate Fees</li>
    <li>Aggressive Defense</li>
    <li>Highly Rated Online</li>
  </ul>
</div>
<a class="abs btn btn-navy" style="left:114px;top:2335px;width:166px;height:44px">LEARN MORE</a>

<svg class="abs" style="left:576px;top:1911px" width="556" height="484" viewBox="0 0 556 484">
  <polygon points="2,241 134,2 422,2 554,241 422,482 134,482" fill="none" stroke="var(--red)" stroke-width="3"/>
  <polygon points="18,241 142,16 414,16 538,241 414,468 142,468" fill="#4a3a30" role="img" aria-label="Team of five attorneys posed in a wood-panelled library office"/>
  <polygon points="18,241 142,16 414,16 538,241 414,468 142,468" fill="url(#hexShade)"/>
  <defs><linearGradient id="hexShade" x1="0" y1="0" x2="0" y2="1"><stop offset="0" stop-color="#2c2420" stop-opacity=".5"/><stop offset="1" stop-color="#6b5a4c" stop-opacity=".5"/></linearGradient></defs>
</svg>

<!-- TESTIMONIALS -->
<section class="abs testi" role="img" aria-label="Faded city skyline background"></section>
<div class="abs center eyebrow" style="top:2524px;font-size:14px">Testimonials</div>
<h2 class="abs center section-title" style="top:2550px">WHAT OUR CLIENTS SAY ABOUT US</h2>
<div class="abs rule" style="left:420px;top:2594px;width:360px"></div>
<div class="abs center" style="top:2626px;color:var(--star);font-size:20px">4.8 ★★★★★</div>
<div class="abs center" style="top:2654px;font-size:22px;color:#5a5f6b;letter-spacing:1px">Verified <span style="font-size:20px">Customer Reviews</span></div>

<div class="abs" style="left:259px;top:2710px;width:620px;height:240px;background:var(--blue)"></div>
<div class="abs" style="left:306px;top:2752px;width:620px;height:244px;background:var(--blue)"></div>
<div class="abs quote-card">
  <svg style="margin-top:36px" width="48" height="34" viewBox="0 0 48 34"><path d="M2 0h18v18L12 34H4l6-16H2zM28 0h18v18l-8 16h-8l6-16h-8z" fill="#9aa0ad"/></svg>
  <p style="font-style:italic;font-size:15.5px;line-height:26px;color:#3a3f4c;margin-top:10px;padding:0 60px">“Sed ut perspiciatis unde omnis iste natus error sit voluptatem accusantium doloremque laudantium totam rem aperiam eaque ipsa quae ab illo inventore veritatis et quasi architecto beatae vitae dicta”</p>
  <div style="font-weight:600;font-size:15px;margin-top:16px">- Dana Ellery</div>
  <div style="color:var(--star);font-size:24px;margin-top:2px;letter-spacing:2px">★★★★★</div>
</div>
<div class="abs round-arrow" style="left:163px;top:2824px"><svg width="12" height="20" viewBox="0 0 12 20"><path d="M10 2 2 10l8 8" stroke="#666" stroke-width="2" fill="none"/></svg></div>
<div class="abs round-arrow" style="left:978px;top:2824px"><svg width="12" height="20" viewBox="0 0 12 20"><path d="M2 2l8 8-8 8" stroke="#666" stroke-width="2" fill="none"/></svg></div>

<!-- BLOGS -->
<div class="abs" style="left:123px;top:3170px">
  <div class="eyebrow">Articles &amp; News</div>
  <h2 class="section-title" style="margin-top:4px">LATEST BLOGS</h2>
  <div class="rule" style="width:230px;margin-top:6px"></div>
</div>

<article class="abs blog" style="left:116px;top:3287px;width:313px;height:383px">
  <div class="blog-img" role="img" aria-label="Businesswoman in an office with colleagues behind her" style="background:linear-gradient(135deg,#c7ccd6,#6b7488)"></div>
  <div class="blog-date">20 APR 2025</div>
  <h4>Sed ut perspiciatis unde omnis iste natus error sit voluptatem</h4>
  <p>Sed ut perspiciatis unde omnis iste natus error sit voluptatem accusantium doloremque laudantium, totam rem aperiam</p>
  <a class="btn">LEARN MORE</a>
</article>
<article class="abs blog" style="left:448px;top:3287px;width:312px;height:383px">
  <div class="blog-img" role="img" aria-label="Hands signing a contract with a gavel on the desk" style="background:linear-gradient(135deg,#d8dbe0,#7d8290)"></div>
  <div class="blog-date">20 APR 2025</div>
  <h4>Sed ut perspiciatis unde omnis iste natus error sit voluptatem</h4>
  <p>Sed ut perspiciatis unde omnis iste natus error sit voluptatem accusantium doloremque laudantium, totam rem aperiam</p>
  <a class="btn">LEARN MORE</a>
</article>
<article class="abs blog" style="left:781px;top:3287px;width:314px;height:383px">
  <div class="blog-img" role="img" aria-label="Lawyers in discussion around a meeting table" style="background:linear-gradient(135deg,#9aa2b2,#3a4254)"></div>
  <div class="blog-date">20 APR 2025</div>
  <h4>Sed ut perspiciatis unde omnis iste natus error sit voluptatem</h4>
  <p>Sed ut perspiciatis unde omnis iste natus error sit voluptatem accusantium doloremque laudantium, totam rem aperiam</p>
  <a class="btn">LEARN MORE</a>
</article>

<!-- FOOTER BASE -->
<footer class="abs footer"></footer>

<!-- CONSULTATION -->
<section class="abs consult">
  <div class="abs eyebrow" style="left:0;width:972px;text-align:center;top:70px;color:#dbe3f4;font-size:14px">Get in touch with us</div>
  <h2 class="abs section-title" style="left:0;width:972px;text-align:center;top:100px;color:var(--white)">REQUEST A FREE CONSULTATION</h2>
  <div class="abs field" style="left:145px;top:195px;width:326px">First Name</div>
  <div class="abs field" style="left:513px;top:199px;width:326px">Last Name</div>
  <div class="abs field" style="left:145px;top:262px;width:326px">Phone number</div>
  <div class="abs field" style="left:513px;top:267px;width:326px">Email address</div>
  <div class="abs field" style="left:145px;top:331px;width:694px;height:63px">Message</div>
  <a class="abs btn btn-red" style="left:413px;top:424px;width:167px;height:42px;border-radius:2px">SUBMIT NOW</a>
</section>

<div class="abs brand" style="left:135px;top:4350px;color:#d6dae3">
  <span class="brand-mark"></span><span class="brand-name">Harlow Bennett</span>
</div>
<nav class="abs foot-nav" style="left:0;top:4357px;width:1200px">
  <a style="left:483px;font-weight:700">HOME</a>
  <a style="left:573px">ABOUT US</a>
  <a style="left:689px">PRACTICE AREAS</a>
  <a style="left:851px">BLOGS</a>
  <a style="left:944px">CONTACT US</a>
</nav>
<div class="abs" style="left:0;top:4445px;width:1200px;height:1px;background:#24335a"></div>
<div class="abs legal" style="left:135px;top:4465px">© 2025 Company Name | All Rights Reserved</div>
<div class="abs legal" style="left:897px;top:4467px">Terms of use &nbsp;&nbsp; Privacy Policy</div>

</body>
</html>
```